Pellowick bottle design

We're a small company looking for someone to help with our bottle design. We provide a sauce that will boost the flavor of packaged ramen. We're looking for a label that will stand out. I'm attaching some of the labels we like and some that I've made.

```html
<!DOCTYPE html>
<html lang="en">
<head>
<meta charset="utf-8">
<title>Pellowick Ramen Sauce Label</title>
<link rel="stylesheet" href="https://fonts.googleapis.com/css2?family=Archivo:wght@500;800&display=swap">
<style>
  :root {
    --label-red: #ec1c24;
    --pattern-tint: #f4777b;
    --ink-white: #ffffff;
    --page: #ffffff;
  }
  html, body {
    margin: 0;
    padding: 0;
    width: 1200px;
    height: 1200px;
    overflow: hidden;
    background: var(--page);
  }
  .canvas {
    position: relative;
    width: 1200px;
    height: 1200px;
  }
  .label {
    position: absolute;
    left: 0;
    top: 0;
    width: 1200px;
    height: 1200px;
  }
  .label-disc { fill: var(--label-red); }
  .noodle-pattern { fill: var(--pattern-tint); }
  .brand-vertical {
    font-family: "Archivo", sans-serif;
    font-weight: 500;
    font-size: 58px;
    fill: var(--ink-white);
    letter-spacing: 0;
  }
  .brand-bold {
    font-family: "Archivo", sans-serif;
    font-weight: 800;
    font-size: 66px;
    fill: var(--ink-white);
  }
  .product-type {
    font-family: "Archivo", sans-serif;
    font-weight: 500;
    font-size: 28px;
    fill: var(--ink-white);
  }
</style>
</head>
<body>
<main class="canvas">
  <svg class="label" viewBox="0 0 1200 1200" xmlns="http://www.w3.org/2000/svg" aria-label="Pellowick ramen sauce label">
    <defs>
      <clipPath id="disc-clip">
        <circle cx="600" cy="600" r="380"/>
      </clipPath>
    </defs>

    <circle class="label-disc" cx="600" cy="600" r="380"/>

    <g clip-path="url(#disc-clip)">
      <path class="noodle-pattern" role="img" aria-label="Decorative noodle loop pattern"
            d="M560 200 L1000 200 L1000 700 Q900 640 820 520 Q720 380 560 260 Z"/>
      <path class="noodle-pattern" role="img" aria-label="Decorative noodle loop pattern"
            d="M200 640 Q290 720 330 820 Q370 920 460 1000 L200 1000 Z"/>
    </g>

    <g class="brand-name">
      <text class="brand-vertical" x="487" y="400" text-anchor="middle">P</text>
      <text class="brand-vertical" x="487" y="490" text-anchor="middle">E</text>
      <text class="brand-vertical" x="487" y="580" text-anchor="middle">L</text>
      <text class="brand-vertical" x="487" y="670" text-anchor="middle">L</text>
      <text class="brand-vertical" x="487" y="760" text-anchor="middle">O</text>
      <text class="brand-bold" x="526" y="822">WICK</text>
    </g>
    <text class="product-type" x="528" y="860">RAMEN SAUCE</text>
  </svg>
</main>
</body>
</html>
```